Australian Software Consultancy needs new Business Card Design

Design Business Card based on existing design artefacts (attached). We are open to all designs. As its a 2 sided design and we thought it might be quite striking to have one side with a black background and te other side with a white background.

Target Market(s)

Financial Services mainly.

Industry/Entity Type

Business

Contact Information for Business Card

Name :
Position :
Email :

Requirements
Must have
• Funky design using our existing assets

```html
<!DOCTYPE html>
<html lang="en">
<head>
<meta charset="UTF-8">
<title>Business Card – Front and Back</title>
<link rel="stylesheet" href="https://fonts.googleapis.com/css2?family=Montserrat:wght@400;500;700;800&display=swap">
<style>
  :root {
    --backdrop: #d6d6d6;
    --ink-black: #060606;
    --paper-white: #eeeeee;
    --accent-red: #e0262b;
    --text-light: #f2f2f2;
    --text-dark: #1a1a1a;
  }
  * { box-sizing: border-box; margin: 0; padding: 0; }
  html, body {
    width: 1200px;
    height: 1000px;
    overflow: hidden;
    background: var(--backdrop);
    font-family: "Montserrat", Arial, sans-serif;
  }
  .canvas {
    position: relative;
    width: 1200px;
    height: 1000px;
  }
  .card {
    position: absolute;
    width: 520px;
    height: 300px;
    box-shadow: 0 4px 12px rgba(0,0,0,0.18);
    overflow: hidden;
  }
  /* Front side */
  .card--front {
    left: 110px;
    top: 120px;
    background: radial-gradient(circle at 35% 25%, #1e1e1e 0%, var(--ink-black) 70%);
    display: flex;
    align-items: center;
    justify-content: center;
  }
  .front-brand {
    display: flex;
    align-items: center;
    gap: 12px;
  }
  .front-brand__dot {
    width: 16px;
    height: 16px;
    border-radius: 50%;
    background: var(--accent-red);
  }
  .front-brand__name {
    color: var(--accent-red);
    font-weight: 800;
    font-size: 26px;
    letter-spacing: 1px;
  }
  /* Back side */
  .card--back {
    left: 570px;
    top: 560px;
    display: flex;
  }
  .back-identity {
    width: 46%;
    background: linear-gradient(160deg, #1a1a1a 0%, var(--ink-black) 60%);
    display: flex;
    flex-direction: column;
    justify-content: flex-end;
    padding: 0 20px 46px 26px;
  }
  .back-identity__name {
    color: var(--text-light);
    font-weight: 500;
    font-size: 15px;
    letter-spacing: 3.5px;
  }
  .back-identity__role {
    color: var(--accent-red);
    font-weight: 500;
    font-size: 11px;
    letter-spacing: 2px;
    margin-top: 4px;
  }
  .back-contact {
    width: 54%;
    background: var(--paper-white);
    display: flex;
    flex-direction: column;
    align-items: center;
    justify-content: center;
    gap: 38px;
    color: var(--text-dark);
  }
  .back-contact__line {
    font-size: 11px;
    font-weight: 500;
    letter-spacing: 2px;
  }
  .back-contact__brand {
    font-weight: 800;
    font-size: 17px;
    color: var(--text-dark);
    letter-spacing: 0.5px;
  }
</style>
</head>
<body>
  <main class="canvas">
    <section class="card card--front" aria-label="Card front">
      <div class="front-brand">
        <span class="front-brand__dot"></span>
        <span class="front-brand__name">NORTHLOOP</span>
      </div>
    </section>

    <section class="card card--back" aria-label="Card back">
      <div class="back-identity">
        <p class="back-identity__name">YOUR NAME HERE</p>
        <p class="back-identity__role">Positions</p>
      </div>
      <div class="back-contact">
        <p class="back-contact__line">+ 62 XXXX XXXX</p>
        <p class="back-contact__brand">NORTHLOOP</p>
        <p class="back-contact__line">email@mail.com</p>
      </div>
    </section>
  </main>
</body>
</html>
```